Web Design Project for SEARCH ENGINE !

We need a website design for torrents search engine.

The Website will be www.Qorvexa.com

Qorvexa is a a search engine for torrents.
Qorvexa search and index torrents results from all torrents sites.

We will need:
Logo
WebSite Design
slogen (optional)

we need only PSDs - no codded pages are needed !

Design to the following screen Size & resolution: 1024 x 768

***PLEASE DOWNLOAD ATTACHED FILE !

```html
<!DOCTYPE html>
<html lang="en">
<head>
<meta charset="utf-8">
<title>Qorvexa – Torrents Search Engine</title>
<link rel="stylesheet" href="https://fonts.googleapis.com/css2?family=Arimo:wght@400;700&display=swap">
<style>
:root{
  --bar-dark:#1f1f1f;
  --green:#3aa83a;
  --green-bright:#46c23a;
  --red:#c8102e;
  --orange:#f08a24;
  --text:#444;
  --muted:#8a8a8a;
  --line:#a9a9a9;
  --panel:#e4e4e4;
  --strip:#c7c7c7;
  --blue:#1ea0dc;
  --seed:#6cbf3a;
  --page:#fbfbfb;
}
*{box-sizing:border-box;margin:0;padding:0}
html,body{width:1164px;height:1200px;overflow:hidden}
body{position:relative;font-family:"Arimo",Arial,sans-serif;color:var(--text);
  background:linear-gradient(#f4f4f4,#ffffff 40%,#f0f0f0);}
.page{position:absolute;left:7px;top:0;width:1149px;height:1200px;background:var(--page);
  box-shadow:0 0 4px rgba(0,0,0,.25)}
.topbar{position:absolute;left:7px;top:4px;width:1149px;height:34px;
  background:linear-gradient(#4a4a4a,var(--bar-dark) 60%,#111);}
.social{position:absolute;top:8px;display:flex;gap:19px}
.social span{display:block;width:18px;height:18px;border-radius:3px}
.social.left{left:21px}
.social.right{left:999px}
.main-nav{position:absolute;left:241px;top:10px;display:flex;color:#fff;font-size:13px;white-space:nowrap}
.main-nav a{color:#fff;text-decoration:none}
.main-nav a.current{color:var(--green-bright)}
.main-nav .sep{margin:0 6px}
.lang{position:absolute;left:841px;top:6px;width:68px;height:22px;background:var(--green);
  color:#fff;font-size:12px;line-height:22px;padding-left:9px}
.lang::after{content:"";position:absolute;right:9px;top:8px;border:4px solid transparent;border-top:5px solid #fff}
.brand{position:absolute;left:20px;top:54px;display:flex;align-items:center;gap:6px}
.brand-dot{width:30px;height:30px;border-radius:50%;background:var(--green)}
.brand-name{font-size:28px;color:#6f6f6f;font-weight:700;letter-spacing:-1px}
.tagline{position:absolute;left:21px;top:94px;font-size:10px;color:#555;letter-spacing:.2px}
.search{position:absolute;left:188px;top:60px;width:786px;height:32px;display:flex}
.search-field{flex:1;background:#d6d6d6;font-size:18px;color:#444;padding:6px 8px}
.search-btn{width:63px;background:#1b1b1b;color:#fff;font-size:10px;display:flex;align-items:center;justify-content:center;gap:3px}
.stats{position:absolute;left:188px;top:97px;font-size:11px;color:#333}
.include{position:absolute;right:190px;top:96px;font-size:11px;color:#333;display:flex;align-items:center;gap:4px}
.include i{display:inline-block;width:11px;height:11px;border:1px solid #555;position:relative}
.include i::after{content:"";position:absolute;left:3px;top:0;width:3px;height:6px;border:solid #333;border-width:0 2px 2px 0;transform:rotate(40deg)}
.filterbar{position:absolute;left:188px;top:127px;width:786px;height:22px;background:#d2d2d2;font-size:10.5px;color:#333;white-space:nowrap}
.filterbar .range{position:absolute;left:6px;top:5px}
.filterbar .order{position:absolute;right:4px;top:5px}
.pager{position:absolute;left:490px;top:124px;width:185px;height:22px;background:#262626;color:#fff;font-size:10.5px;
  text-align:center;line-height:22px;border-radius:3px 3px 0 0;white-space:nowrap}
.pager .on{color:var(--green-bright)}
.qualitybar{position:absolute;left:188px;top:152px;width:786px;height:19px;background:var(--strip);font-size:10.5px;color:#333;
  text-align:center;line-height:19px;padding-left:80px;white-space:nowrap}
.hl{color:var(--red)}
.results{position:absolute;left:188px;width:786px;list-style:none}
.results.main{top:186px}
.results.related{top:722px}
.result{position:relative;height:37px;border-bottom:1px solid var(--line);font-size:13.5px;white-space:nowrap}
.result > *{position:absolute;top:11px;white-space:nowrap}
.r-title{left:0;color:#444}
.r-site{left:392px;width:0;display:flex;justify-content:center;font-size:11px;color:var(--red);top:13px}
.r-status{left:531px;top:12px;width:14px;height:14px;border-radius:50%;border:2px solid}
.r-status.ok{border-color:var(--green);color:var(--green)}
.r-status.bad{border-color:var(--red);color:var(--red)}
.r-status.mid{border-color:var(--orange);background:radial-gradient(circle,var(--orange) 3px,#fff 3.5px)}
.r-status.ok::before,.r-status.ok::after,.r-status.bad::before{content:"";position:absolute;left:2px;top:4px;width:6px;height:2px;background:currentColor}
.r-status.ok::after{transform:rotate(90deg)}
.r-age{left:561px;font-size:11px;color:var(--muted);top:13px}
.r-size{left:629px;font-size:11px;color:var(--muted);top:13px}
.badge{display:inline-block;width:13px;height:13px;color:#fff;font-size:10px;font-style:normal;text-align:center;line-height:13px;margin-right:3px;vertical-align:-2px}
.r-peers,.r-seeds{font-size:11px;color:var(--muted);top:12px}
.r-peers{left:676px}
.r-seeds{left:740px}
.r-peers .badge{background:var(--blue)}
.r-seeds .badge{background:var(--seed)}
.related-head{position:absolute;left:188px;top:683px;width:786px;height:22px;background:var(--panel);
  color:var(--red);font-size:13.5px;line-height:22px;padding-left:8px}
.comment{position:absolute;left:188px;top:926px;width:786px;height:186px;background:var(--panel)}
.comment-title{position:absolute;left:39px;top:0;width:145px;height:30px;background:#1d1d1d;color:#fff;font-size:14px;
  line-height:30px;text-align:center;box-shadow:2px 2px 3px rgba(0,0,0,.3)}
.comment-box{position:absolute;left:40px;top:40px;width:706px;height:107px;background:#fff}
.btn{position:absolute;top:156px;width:73px;height:21px;background:#1d1d1d;color:#fff;font-size:13px;text-align:center;line-height:21px}
.btn.clear{left:586px}
.btn.submit{left:674px}
.footer{position:absolute;left:7px;top:1160px;width:1149px;height:34px;background:linear-gradient(#444,var(--bar-dark) 50%,#111);
  color:#fff;font-size:11.5px;text-align:center;line-height:34px;white-space:nowrap}
.footer a{color:var(--green-bright);text-decoration:none}
</style>
</head>
<body>
<div class="page"></div>

<header class="topbar">
  <div class="social left">
    <span style="background:#3b5b9a"></span><span style="background:#3aa0d8"></span><span style="background:#e9761d"></span><span style="background:#2f6fb4"></span>
  </div>
  <nav class="main-nav">
    <a class="current" href="#">HOME</a><span class="sep">|</span>
    <a href="#">ABOUT US</a><span class="sep">|</span>
    <a href="#">TORRENT SEARCH</a><span class="sep">|</span>
    <a href="#">SITE SEARCH</a><span class="sep">|</span>
    <a href="#">HELP</a><span class="sep">|</span>
    <a href="#">LOGIN</a><span class="sep">|</span>
    <a href="#">SIGNIN</a>
  </nav>
  <div class="lang">English</div>
  <div class="social right">
    <span style="background:#dfe6ee"></span><span style="background:#d9d9d9"></span><span style="background:#b9c94a"></span><span style="background:#c02a2a"></span>
  </div>
</header>

<div class="brand"><span class="brand-dot"></span><span class="brand-name">Qorvexa</span></div>
<div class="tagline">TORRENTS SEARCH ENGINE</div>

<form class="search">
  <div class="search-field">starforge 3</div>
  <div class="search-btn">
    <svg width="9" height="9" viewBox="0 0 10 10"><circle cx="4" cy="4" r="3" fill="none" stroke="#fff" stroke-width="1.5"/><line x1="6" y1="6" x2="9.5" y2="9.5" stroke="#fff" stroke-width="1.5"/></svg>SEARCH
  </div>
</form>
<div class="stats">About 50,000 results (0.12 seconds)</div>
<div class="include">Sites search include <i></i></div>

<div class="filterbar">
  <span class="range">1 - 10 of 20 for " starforge 3 " ( 1,155s )</span>
  <span class="order">Order by : | <span class="hl">name</span> | date | size | peers | seeds</span>
</div>
<div class="pager">previous | 1 | 2 | <span class="on">3</span> | 4 | next</div>
<div class="qualitybar">Quality : | <span class="hl">all</span> | good | bad | verified &nbsp;&nbsp;&nbsp; Search by : | filename | <span class="hl">titles</span> | data added</div>

<ul class="results main">
  <li class="result"><span class="r-title">starforge 3  HD XVD bgfsbsb.225</span><span class="r-site">seedharbor.com</span><span class="r-status ok"></span><span class="r-age">3 days ago</span><span class="r-size">549 MB</span><span class="r-peers"><i class="badge">P</i>10.555</span><span class="r-seeds"><i class="badge">S</i>10.200</span></li>
  <li class="result"><span class="r-title">starforge 3  HD XVD bgfsbsb.225</span><span class="r-site">kelvado.eu</span><span class="r-status bad"></span><span class="r-age">3 days ago</span><span class="r-size">549 MB</span><span class="r-peers"><i class="badge">P</i>10.555</span><span class="r-seeds"><i class="badge">S</i>10.200</span></li>
  <li class="result"><span class="r-title">starforge 3  HD XVD bgfsbsb.225</span><span class="r-site">yourpeerfile.com</span><span class="r-status ok"></span><span class="r-age">3 days ago</span><span class="r-size">549 MB</span><span class="r-peers"><i class="badge">P</i>10.555</span><span class="r-seeds"><i class="badge">S</i>10.200</span></li>
  <li class="result"><span class="r-title">starforge 3  HD XVD bgfsbsb.225</span><span class="r-site">torrentlume.com</span><span class="r-status ok"></span><span class="r-age">3 days ago</span><span class="r-size">549 MB</span><span class="r-peers"><i class="badge">P</i>10.555</span><span class="r-seeds"><i class="badge">S</i>10.200</span></li>
  <li class="result"><span class="r-title">starforge 3  HD XVD bgfsbsb.225</span><span class="r-site">bitwhisk.com</span><span class="r-status bad"></span><span class="r-age">3 days ago</span><span class="r-size">549 MB</span><span class="r-peers"><i class="badge">P</i>10.555</span><span class="r-seeds"><i class="badge">S</i>10.200</span></li>
  <li class="result"><span class="r-title">starforge 3  HD XVD bgfsbsb.225</span><span class="r-site">seedharbor.com</span><span class="r-status mid"></span><span class="r-age">3 days ago</span><span class="r-size">549 MB</span><span class="r-peers"><i class="badge">P</i>10.555</span><span class="r-seeds"><i class="badge">S</i>10.200</span></li>
  <li class="result"><span class="r-title">starforge 3  HD XVD bgfsbsb.225</span><span class="r-site">kelvado.eu</span><span class="r-status ok"></span><span class="r-age">3 days ago</span><span class="r-size">549 MB</span><span class="r-peers"><i class="badge">P</i>10.555</span><span class="r-seeds"><i class="badge">S</i>10.200</span></li>
  <li class="result"><span class="r-title">starforge 3  HD XVD bgfsbsb.225</span><span class="r-site">yourpeerfile.com</span><span class="r-status ok"></span><span class="r-age">3 days ago</span><span class="r-size">549 MB</span><span class="r-peers"><i class="badge">P</i>10.555</span><span class="r-seeds"><i class="badge">S</i>10.200</span></li>
  <li class="result"><span class="r-title">starforge 3  HD XVD bgfsbsb.225</span><span class="r-site">torrentlume.com</span><span class="r-status mid"></span><span class="r-age">3 days ago</span><span class="r-size">549 MB</span><span class="r-peers"><i class="badge">P</i>10.555</span><span class="r-seeds"><i class="badge">S</i>10.200</span></li>
  <li class="result"><span class="r-title">starforge 3  HD XVD bgfsbsb.225</span><span class="r-site">bitwhisk.com</span><span class="r-status bad"></span><span class="r-age">3 days ago</span><span class="r-size">549 MB</span><span class="r-peers"><i class="badge">P</i>10.555</span><span class="r-seeds"><i class="badge">S</i>10.200</span></li>
  <li class="result"><span class="r-title">starforge 3  HD XVD bgfsbsb.225</span><span class="r-site">seedharbor.com</span><span class="r-status mid"></span><span class="r-age">3 days ago</span><span class="r-size">549 MB</span><span class="r-peers"><i class="badge">P</i>10.555</span><span class="r-seeds"><i class="badge">S</i>10.200</span></li>
  <li class="result"><span class="r-title">starforge 3  HD XVD bgfsbsb.225</span><span class="r-site">kelvado.eu</span><span class="r-status ok"></span><span class="r-age">3 days ago</span><span class="r-size">549 MB</span><span class="r-peers"><i class="badge">P</i>10.555</span><span class="r-seeds"><i class="badge">S</i>10.200</span></li>
  <li class="result"><span class="r-title">starforge 3  HD XVD bgfsbsb.225</span><span class="r-site">yourpeerfile.com</span><span class="r-status ok"></span><span class="r-age">3 days ago</span><span class="r-size">549 MB</span><span class="r-peers"><i class="badge">P</i>10.555</span><span class="r-seeds"><i class="badge">S</i>10.200</span></li>
</ul>

<div class="related-head">starforge 3 &nbsp;related torrents</div>

<ul class="results related">
  <li class="result"><span class="r-title">starforge 3  HD XVD bgfsbsb.225</span><span class="r-site">torrentlume.com</span><span class="r-status mid"></span><span class="r-age">3 days ago</span><span class="r-size">549 MB</span><span class="r-peers"><i class="badge">P</i>10.555</span><span class="r-seeds"><i class="badge">S</i>10.200</span></li>
  <li class="result"><span class="r-title">starforge 3  HD XVD bgfsbsb.225</span><span class="r-site">bitwhisk.com</span><span class="r-status bad"></span><span class="r-age">3 days ago</span><span class="r-size">549 MB</span><span class="r-peers"><i class="badge">P</i>10.555</span><span class="r-seeds"><i class="badge">S</i>10.200</span></li>
  <li class="result"><span class="r-title">starforge 3  HD XVD bgfsbsb.225</span><span class="r-site">seedharbor.com</span><span class="r-status mid"></span><span class="r-age">3 days ago</span><span class="r-size">549 MB</span><span class="r-peers"><i class="badge">P</i>10.555</span><span class="r-seeds"><i class="badge">S</i>10.200</span></li>
  <li class="result"><span class="r-title">starforge 3  HD XVD bgfsbsb.225</span><span class="r-site">kelvado.eu</span><span class="r-status ok"></span><span class="r-age">3 days ago</span><span class="r-size">549 MB</span><span class="r-peers"><i class="badge">P</i>10.555</span><span class="r-seeds"><i class="badge">S</i>10.200</span></li>
  <li class="result"><span class="r-title">starforge 3  HD XVD bgfsbsb.225</span><span class="r-site">yourpeerfile.com</span><span class="r-status ok"></span><span class="r-age">3 days ago</span><span class="r-size">549 MB</span><span class="r-peers"><i class="badge">P</i>10.555</span><span class="r-seeds"><i class="badge">S</i>10.200</span></li>
</ul>

<section class="comment">
  <div class="comment-title">POST A COMMENT</div>
  <div class="comment-box"></div>
  <div class="btn clear">CLEAR</div>
  <div class="btn submit">SUBMIT</div>
</section>

<footer class="footer">COPYRIGHT © 2011 QORVEXA. USE OF THIS WEBSITE CONSTITUTES ACCEPTANCE OF OUR <a href="#">USER AGREEMENT</a> AND <a href="#">PRIVACY POLICY</a>.</footer>
</body>
</html>
```